Geschäftspapier RVW
Sehr kreative Herangehensweise an das Projekt und sehr gute Zusammenarbeit. Gerne wieder!
Zielgruppe
In den letzten Jahren konnten wir uns durch viel Engagement und Ehrgeiz zum Marktführer im Bereich Kaschierungen und Beschichtungen für den Automobilinnenraum in Europa entwickeln. Angeboten werden Rollenware sowie der Zuschnitt und die Weiterverarbeitung von kaschierten Verbundmaterialien und deren Entwicklung für den jeweiligen Einsatzzweck.
Die vielseitig hergestellten Verbundmaterialien aus Textil bis hin zu Kunst- und Echtledern findet man heute in vielen Bauteilen namhafter Automarken, der Flugzeug- und Schienenfahrzeugindustrie sowie in weiteren industriellen, technischen Anwendungen.
Beispiele dafür sind Innenverkleidungen und Sitze im Fahrzeug, Sonnenschutzkomponenten für den privaten und industriellen Bedarf, wie auch Bezüge von Kindersitzen oder medizinische Hygieneprodukte.
Aufgabenstellung
Zur Darstellung des Unternehmens wird ein neues Geschäftspapier gesucht. Dies sollte die folgenden Informationen zum Unternehmen, sowie die Bankkontakte enthalten. Ebenso sollte das vorhandene Firmenlogo integriert werden.
Das Unternehmen produziert hochwertige Textil-Produkte aus den Bereichen Automarken, der Flugzeug- und Schienenfahrzeugindustrie sowie in weiteren industriellen, technischen Anwendungen.
Das Geschäftspapier sollte diese Eigenschaft widerspiegeln und luxuriös, sowie modern erscheinen.
[Optional]
145 Jahre Erfahrung in der Textilveredlung - Führende Kaschier- und Beschichtungstechnologie
145 years of experience in textile processing - Leading technology in lamination and coating
Unternehmensfarbe Grün:
HKS 61 K
70% Cyan
0% Magenta
100% Gelb
75 % Schwarz
optionale Werbefarbe Anthrazit:
77% Cyan
72% Magenta
67% Gelb
84% Schwarz
Schriftart:
Arial

```html
<!DOCTYPE html>
<html lang="de">
<head>
<meta charset="utf-8">
<title>Geschäftspapier RVW</title>
<link rel="stylesheet" href="https://fonts.googleapis.com/css2?family=Arimo:ital,wght@0,400;0,700;1,400&display=swap">
<style>
  :root {
    --brand-green: #234a25;
    --ink: #111111;
    --paper: #ffffff;
    --panel-text: #ffffff;
  }
  html, body { margin: 0; padding: 0; overflow: hidden; background: var(--paper); }
  .letter {
    position: relative;
    width: 844px; height: 1200px;
    overflow: hidden;
    background: var(--paper);
    font-family: "Arimo", Arial, sans-serif;
    color: var(--ink);
  }
  .sidebar {
    position: absolute; left: 627px; top: 0;
    width: 217px; height: 1200px;
    background: var(--brand-green);
    color: var(--panel-text);
  }
  .sidebar-notch { position: absolute; left: 600px; top: 81px; }
  .company-info {
    position: absolute; left: 29px; top: 57px;
    font-size: 12.3px; line-height: 19.65px;
    margin: 0;
  }
  .company-info p { margin: 0; }
  .company-info .gap { height: 19.65px; }
  .bank-list { position: absolute; left: 27px; top: 684px; font-size: 12.3px; line-height: 19.65px; }
  .bank-label { font-size: 11.5px; margin: 0 0 4px; }
  .bank { margin: 0 0 11px; }
  .bank p { margin: 0; }
  .bank-name { font-weight: 700; }

  .wordmark {
    position: absolute; left: 48px; top: 76px;
    margin: 0;
    font-size: 62px; font-weight: 400; letter-spacing: 1px;
    color: var(--brand-green);
  }

  .recipient {
    position: absolute; left: 45px; top: 233px;
    font-size: 15.6px; line-height: 20.3px; margin: 0;
  }
  .recipient p { margin: 0; }
  .recipient .recipient-name { color: var(--brand-green); }

  .subject-row {
    position: absolute; left: 45px; top: 362px; width: 539px;
    display: flex; justify-content: space-between;
    font-size: 15.6px;
  }
  .subject { font-weight: 700; margin: 0; }
  .date { margin: 0; }

  .body {
    position: absolute; left: 45px; top: 403px; width: 539px;
    font-size: 15.6px; line-height: 20.25px;
  }
  .body p { margin: 0 0 20.25px; text-align: justify; }
  .body .salutation { margin-bottom: 16px; text-align: left; }

  .claim {
    position: absolute; left: 30px; top: 1113px; width: 570px;
    text-align: center; color: var(--brand-green);
    font-size: 11.6px; line-height: 15.3px;
  }
  .claim p { margin: 0; }
  .claim .claim-en { font-style: italic; }
</style>
</head>
<body>
<div class="letter">
  <h1 class="wordmark">R. V. Weldner</h1>

  <svg class="sidebar-notch" width="28" height="52" viewBox="0 0 28 52" aria-hidden="true">
    <polygon points="28,0 0,26 28,52" fill="var(--brand-green)"/>
  </svg>
  <aside class="sidebar">
    <div class="company-info">
      <p>Adresse:</p>
      <p>R. V. Weldner GmbH</p>
      <p>Industriering 4</p>
      <p>D-08412 Talbrunn</p>
      <div class="gap"></div>
      <p>Postanschrift</p>
      <p>Postfach 2290</p>
      <p>D-08430 Felsach</p>
      <div class="gap"></div>
      <p>Phone: +49 3700 5512 0</p>
      <p>Fax: +49 3700 5512 199</p>
      <div class="gap"></div>
      <p>Internet: www.rvweldner.example</p>
      <p>E-Mail: post@rvweldner.example</p>
      <div class="gap"></div>
      <p>Handelsregister:</p>
      <p>HRB 5816 AG Talbrunn</p>
      <p>UStIDNr.: DE 208774310</p>
      <div class="gap"></div>
      <p>Geschäftsführer:</p>
      <p>Jonas Kelber</p>
      <p>Prokura:</p>
      <p>Lena Kelber, Anton Reiß</p>
    </div>

    <div class="bank-list">
      <p class="bank-label">Bankverbindungen:</p>
      <div class="bank">
        <p class="bank-name">Sparkasse Talgrund</p>
        <p>IBAN: DE12 3456 7000 1122</p>
        <p>0033 44</p>
        <p>BIC: TALGDE11XXX</p>
      </div>
      <div class="bank">
        <p class="bank-name">Handelsbank Felsach</p>
        <p>IBAN: DE48 3456 8000 0561</p>
        <p>0274 00</p>
        <p>BIC: HNDLDEFFXXX</p>
      </div>
      <div class="bank">
        <p class="bank-name">Landbank Oberau</p>
        <p>IBAN: DE91 3456 9011 0045</p>
        <p>7123 08</p>
        <p>BIC: LNDBDEMM210</p>
      </div>
      <div class="bank">
        <p class="bank-name">Bürgerbank Oberau</p>
        <p>IBAN: DE37 3457 0122 0418</p>
        <p>0067 52</p>
        <p>BIC: BUERDEF1OB1</p>
      </div>
      <div class="bank">
        <p class="bank-name">Nordbank Talbrunn</p>
        <p>IBAN: DE26 3457 1000 0702</p>
        <p>0385 00</p>
        <p>BIC: NORDDE8TXXX</p>
      </div>
    </div>
  </aside>

  <address class="recipient">
    <p class="recipient-name">Max Mustermann</p>
    <p>Mustermannstr. 12</p>
    <p>12345 Musterstatd</p>
    <p>Deutschland</p>
  </address>

  <div class="subject-row">
    <p class="subject">Dies ist eine Betreffzeile</p>
    <p class="date">Montag, 11. Januar 2016</p>
  </div>

  <div class="body">
    <p class="salutation">Sehr geehrte Damen und Herren,</p>
    <p>Lorem ipsum dolor sit amet, consetetur sadipscing elitr, sed diam nonumy eirmod tempor invidunt ut labore et dolore magna aliquyam erat, sed diam voluptua. At vero eos et accusam et justo duo dolores et ea rebum. Stet clita kasd gubergren, no sea takimata sanctus est Lorem ipsum dolor sit amet. Lorem ipsum dolor sit amet, consetetur sadipscing elitr, sed diam nonumy eirmod tempor invidunt ut labore et dolore magna aliquyam erat, sed diam voluptua. At vero eos et accusam et justo duo dolores et ea rebum. Stet clita kasd gubergren, no sea takimata sanctus est Lorem ipsum dolor sit amet. Lorem ipsum dolor sit amet, consetetur sadipscing elitr, sed diam nonumy eirmod tempor invidunt ut labore et dolore magna aliquyam erat, sed diam voluptua. At vero eos et accusam et justo duo dolores et ea rebum. Stet clita kasd gubergren, no sea takimata sanctus est Lorem ipsum dolor sit amet.</p>
    <p>Duis autem vel eum iriure dolor in hendrerit in vulputate velit esse molestie consequat, vel illum dolore eu feugiat nulla facilisis at vero eros et accumsan et iusto odio dignissim qui blandit praesent luptatum zzril delenit augue duis dolore te feugait nulla facilisi. Lorem ipsum dolor sit amet, consectetuer adipiscing elit, sed diam nonummy nibh euismod tincidunt ut laoreet dolore magna aliquam erat volutpat.</p>
    <p>Ut wisi enim ad minim veniam, quis nostrud exerci tation ullamcorper suscipit lobortis nisl ut aliquip ex ea commodo consequat. Duis autem vel eum iriure dolor in hendrerit in vulputate velit esse molestie consequat, vel illum dolore eu feugiat nulla facilisis at vero eros et accumsan et iusto odio dignissim qui blandit praesent luptatum zzril delenit augue duis dolore te feugait nulla facilisi.</p>
    <p style="text-align:left">Nam liber tempor cum soluta nobis eleifend option congue nihil imperdiet doming id quod mazim placerat facer</p>
  </div>

  <footer class="claim">
    <p>145 Jahre Erfahrung in der Textilveredlung - Führende Kaschier- und Beschichtungstechnologie</p>
    <p class="claim-en">145 years of experience in textile processing - Leading technology in lamination and coating</p>
  </footer>
</div>
</body>
</html>
```